Night Dresses business cards business requirers

We are a new company initiating Mexico operations. Our core business is Night woman dress (both formal and party dress) for rent. Gownvella is the name of the company. ITS Gownvella form by two word. The dress word and topia (Utopic) so the place Gownvella Means That You cant get the ideal, perfect and unique dress for your event. So we would like a modern, very creative, and attractive business card.

Industry/Entity Type

Womens Clothing

Contact Information for Business Card

Rounded Borders, two faces

Requirements
Must have
• Rounded borders, logo and slogan, modern, glam, attractive design
Should not have
• modern design classic or not

```html
<!DOCTYPE html>
<html lang="en">
<head>
<meta charset="utf-8">
<title>Gownvella Business Cards</title>
<link href="https://fonts.googleapis.com/css2?family=Open+Sans:wght@400;600&display=swap" rel="stylesheet">
<style>
  :root {
    --bg: #2b3038;
    --card-dark: #141414;
    --card-dark-soft: #2a2a2a;
    --card-light: #ffffff;
    --orchid: #b8639b;
    --ink: #4a4a4a;
    --ink-light: #cfcfcf;
    --veil: #e4e2e3;
  }
  * { margin: 0; padding: 0; box-sizing: border-box; }
  html, body { width: 1200px; height: 938px; overflow: hidden; }
  body {
    background: var(--bg);
    display: flex;
    align-items: center;
    justify-content: center;
    gap: 40px;
  }
  .card {
    position: relative;
    width: 540px;
    height: 316px;
    border-radius: 24px;
    overflow: hidden;
    box-shadow: 0 18px 40px rgba(0,0,0,.45);
  }

  /* Front face */
  .card--front { background: var(--card-dark); }
  .front-photo {
    position: absolute; inset: 0;
    background:
      radial-gradient(ellipse at 70% 60%, var(--card-dark-soft) 0%, rgba(20,20,20,0) 60%),
      linear-gradient(160deg, #0e0e0e 0%, #1c1c1c 55%, #262626 100%);
  }
  .front-brand {
    position: absolute; inset: 0;
    display: flex; align-items: center; justify-content: center; gap: 18px;
  }

  /* Brand name */
  .brand-dot {
    width: 56px; height: 56px;
    border: 3px solid var(--orchid);
    border-radius: 50%;
    flex: none;
  }
  .brand-name {
    font-family: "Open Sans", sans-serif;
    font-weight: 400;
    font-size: 26px;
    letter-spacing: 3px;
  }
  .card--front .brand-name { color: var(--ink-light); }
  .card--back .brand-name { color: var(--ink); }

  /* Back face */
  .card--back { background: var(--card-light); }
  .back-photo {
    position: absolute; top: 0; right: 0; width: 250px; height: 262px;
    background: linear-gradient(100deg, rgba(255,255,255,1) 0%, var(--veil) 45%, #d6d3d5 70%, var(--veil) 100%);
  }
  .back-brand {
    position: absolute; top: 92px; right: 40px;
    display: flex; align-items: center; gap: 14px;
  }
  .back-brand .brand-dot { width: 62px; height: 62px; }
  .back-brand .brand-name { font-size: 24px; }
  .contact {
    position: absolute; left: 44px; top: 160px;
    font-family: "Open Sans", sans-serif;
    color: var(--ink);
    text-transform: uppercase;
  }
  .contact-phone { font-size: 22px; letter-spacing: 2px; }
  .contact-mail { font-size: 17px; letter-spacing: 1px; margin-top: 6px; }
  .address-band {
    position: absolute; left: 0; right: 0; bottom: 0; height: 54px;
    background: var(--orchid);
    display: flex; align-items: center; justify-content: center; gap: 8px;
    font-family: "Open Sans", sans-serif;
    font-size: 13px;
    letter-spacing: 1px;
    color: #fff;
    text-transform: uppercase;
  }
</style>
</head>
<body>
  <section class="card card--front" aria-label="Card front">
    <div class="front-photo" role="img" aria-label="Dark black-and-white fashion photo of a woman in a flowing evening gown"></div>
    <div class="front-brand">
      <span class="brand-dot"></span>
      <span class="brand-name">Gownvella</span>
    </div>
  </section>

  <section class="card card--back" aria-label="Card back">
    <div class="back-photo" role="img" aria-label="Faded photo of a woman in a sheer white tulle gown"></div>
    <div class="back-brand">
      <span class="brand-dot"></span>
      <span class="brand-name">Gownvella</span>
    </div>
    <div class="contact">
      <p class="contact-phone">00-0123456789</p>
      <p class="contact-mail">info@email.com</p>
    </div>
    <div class="address-band">
      <svg width="11" height="14" viewBox="0 0 12 16" aria-hidden="true">
        <path d="M6 0C2.7 0 0 2.6 0 5.9 0 10.3 6 16 6 16s6-5.7 6-10.1C12 2.6 9.3 0 6 0zm0 8.2a2.3 2.3 0 1 1 0-4.6 2.3 2.3 0 0 1 0 4.6z" fill="#fff"/>
      </svg>
      <span>Lorem ipsum is simply dummy text of the printing</span>
    </div>
  </section>
</body>
</html>
```